Wordpress Design Project - Development Company

We need a website for our Developments company "KT Developments". I would like to use Wordpress for its simplicity to update and added features.
We develop/build and sell Townhouses/Houses and Land around Brisbane, Qld. Initially we require a Web presence with no advanced features. We will develop the user logins and other features at a future point in time. We are undecided on having a single page with most of the detail or to have more detail on linked pages, we will review the options put forward. We have added a Sitemap and possible Frontpage sketch
Some sites for examples we have thought work similar and well:
http://www.brimfield.com.au/index.htm
http://tallowmeadow.com.au/
http://www.pmcorrigan.com.au
http://nexcrafta.com.au/
http://www.halvery.com.au/queensland.aspx
http://www.orbelyne.com.au/
I've attached our newly created Business Cards and we are also working on a logo for the company within the next couple of days which may or may not be the same as the Business Card
Any questions please ask
Updates
Please update the main picture on your webpages to the attached so we can compare equally http://files.quillbox.net/u/55720194/Img1c.jpg
Target Market(s)
Townhouse/House/Land buyers & Salespeople
Industry/Entity Type
Business
Look and feel

```html
<!DOCTYPE html>
<html lang="en">
<head>
<meta charset="utf-8">
<title>KT Developments P/L</title>
<link href="https://fonts.googleapis.com/css2?family=Alfa+Slab+One&family=Arimo:wght@400;700&family=Comfortaa:wght@400;700&family=Open+Sans:wght@400;600&display=swap" rel="stylesheet">
<style>
:root{
  --black:#000;
  --ink:#222;
  --grey-text:#555;
  --light:#f6f6f6;
  --line:#c9c9c9;
  --orange:#f07a1a;
  --orange-deep:#e8681b;
  --red-link:#c4161c;
  --footer:#151515;
  --white:#fff;
}
*{box-sizing:border-box;margin:0;padding:0}
html,body{width:1120px;height:1200px;overflow:hidden}
body{position:relative;background:var(--white);font-family:"Arimo",Arial,sans-serif;color:var(--ink)}
.abs{position:absolute}

/* header */
.topbar{left:0;top:0;width:1120px;height:491px;background:var(--black)}
.brandbar{left:0;top:25px;width:1120px;height:55px;background:linear-gradient(#262626,#0a0a0a 60%,#111);border-top:1px solid #333;border-bottom:1px solid #333}
.brand-band{left:0;top:25px;width:418px;height:55px;background:linear-gradient(90deg,#6e6e6e,#d8d8d8 20%,#f4f4f4 45%,#cfcfcf 75%,#9a9a9a)}
.brand-name{left:438px;top:40px;font-family:"Open Sans",sans-serif;font-size:22px;letter-spacing:5px;color:#e6e6e6}
.search{left:816px;top:40px;width:136px;height:26px;background:var(--white);border-radius:4px;font-family:"Open Sans",sans-serif;font-size:11px;color:#999;padding:6px 0 0 19px}
.search svg{position:absolute;right:11px;top:8px}

/* hero */
.hero{left:160px;top:99px;width:800px;height:392px;background:linear-gradient(180deg,#bfd9ef 0%,#e4eef6 30%,#d8b59a 62%,#8c8a97 100%)}
.hero-panel{left:176px;top:153px;width:223px;height:282px;background:rgba(70,72,66,.88);border:2px solid #8d8d86;border-radius:3px;box-shadow:0 0 6px rgba(0,0,0,.5)}
.hero-title{left:182px;top:178px;width:214px;text-align:center;font-family:"Alfa Slab One",serif;font-weight:400;font-size:14.5px;line-height:29px;color:var(--orange)}
.hero-text{left:200px;top:240px;width:192px;font-family:"Open Sans",sans-serif;font-size:13px;line-height:24px;color:var(--white)}
.dots-tab{left:512px;top:461px;width:157px;height:30px;background:var(--white);border-radius:3px 3px 0 0;display:flex;gap:4px;padding:5px 0 0 8px}
.dot{width:20px;height:20px;border-radius:50%;background:radial-gradient(circle at 40% 35%,#555,#1b1b1b)}
.dot.on{background:radial-gradient(circle at 40% 35%,#ffb050,#ef7f12)}

/* nav */
.nav{left:0;top:491px;width:1120px;height:44px;background:linear-gradient(#fdfdfd,#e3e3e3);border-bottom:1px solid #d2d2d2}
.nav ul{position:absolute;left:204px;top:0;list-style:none;display:flex;height:44px}
.nav li{font-family:"Open Sans",sans-serif;font-size:10.5px;color:#222;line-height:48px;padding:0 12px;border-right:1px solid #d5d5d5}
.nav li:last-child{border-right:0}
.dropdown{left:260px;top:535px;width:151px;height:70px;background:#a9a9a9;z-index:3}
.drop-item{position:absolute;left:8px;width:137px;height:24px;background:linear-gradient(#fff,#e6e6e6);border-radius:3px;font-family:"Open Sans",sans-serif;font-size:10px;color:#222;padding:6px 0 0 11px}

/* cards */
.card{top:551px;width:207px;height:227px;border:1px solid #bdbdbd;border-radius:4px;background:linear-gradient(#fff,#e6e6e6)}
.card.dark{background:linear-gradient(#4a4a4a,#000);border-color:#222}
.card h3{position:absolute;top:15px;width:100%;text-align:center;font-family:"Open Sans",sans-serif;font-weight:400;font-size:12.5px;color:#111}
.card.dark h3{color:var(--orange)}
.card .photo{position:absolute;left:18px;top:36px;width:171px;height:93px;border-radius:4px;border:1px solid #222}
.card.dark .photo{border-color:var(--orange)}
.card h4{position:absolute;left:37px;top:140px;font-family:"Open Sans",sans-serif;font-weight:400;font-size:10px;color:#333}
.card.dark h4{color:var(--orange)}
.card p{position:absolute;left:37px;top:156px;width:150px;font-size:10px;line-height:11.5px;color:#222}
.card.dark p{color:var(--white)}
.card .more{position:absolute;left:41px;top:196px;font-family:"Open Sans",sans-serif;font-size:10px;color:#333}
.card.dark .more{color:var(--orange)}

/* welcome */
.welcome{left:0;top:803px;width:1120px;height:251px;background:linear-gradient(#f2f2f2,#fbfbfb)}
.welcome-title{left:218px;top:820px;font-family:"Comfortaa",sans-serif;font-weight:400;font-size:15px;color:#333}
.welcome-title b{font-size:23px;font-weight:400}
.welcome-photo{left:172px;top:864px;width:254px;height:162px;background:linear-gradient(180deg,#6fa3dc 0%,#d7e6f3 40%,#c9c7bd 60%,#6e9a4c 80%,#8da86a 100%)}
.welcome-text{left:439px;top:873px;width:268px;font-size:10.2px;line-height:16.8px;color:#333}
.link-more{font-family:"Open Sans",sans-serif;font-size:11px;color:var(--red-link)}
.link-more span{font-size:9px;margin-right:6px}
.divider{left:716px;top:823px;width:2px;height:213px;background:#cfcfcf}
.cat-title{left:777px;top:832px;font-family:"Comfortaa",sans-serif;font-weight:700;font-size:13px;color:#444;letter-spacing:-.3px}
.cats{left:760px;top:866px;list-style:none}
.cats li{font-size:10.5px;color:#666;height:24.8px;display:flex;align-items:flex-start;gap:10px}
.cats li::before{content:"";width:4px;height:4px;margin-top:3px;border-top:2px solid var(--orange);border-right:2px solid var(--orange);transform:rotate(45deg)}

/* footer */
.footer{left:0;top:1054px;width:1120px;height:146px;background:var(--footer)}
.fsep{top:1065px;width:0;height:127px;border-left:1px dotted #555}
.ftitle{font-family:"Arimo",sans-serif;font-weight:400;font-size:17px;color:var(--white)}
.ftitle em{font-style:normal;color:var(--orange)}
.faddr-h{left:212px;top:1093px;font-family:"Open Sans",sans-serif;font-weight:600;font-size:12px;color:var(--orange-deep)}
.faddr{left:213px;top:1109px;width:95px;font-size:10px;line-height:16px;color:#aaa}
.phone{left:216px;font-family:"Open Sans",sans-serif;font-weight:600;font-size:13px;color:var(--white)}
.social{left:494px;top:1095px;display:flex;gap:11px}
.social i{display:block;width:21px;height:21px;border-radius:50%}
.flinks{left:423px;top:1143px;font-size:9.5px;color:#aaa}
.copy{left:435px;top:1166px;font-size:9.5px;color:#aaa}
.flabel{font-size:10px;color:#999;text-align:right;width:80px}
.finput{left:809px;width:111px;height:20px;background:#bdbdbd;border:1px solid #e0e0e0}
.subscribe{left:812px;top:1163px;width:83px;height:23px;border-radius:4px;background:linear-gradient(#3c3c3c,#141414);font-size:10.5px;color:var(--white);text-align:center;line-height:23px}
</style>
</head>
<body>

<header>
  <div class="abs topbar"></div>
  <div class="abs brandbar"></div>
  <div class="abs brand-band"></div>
  <div class="abs brand-name">KT Developments P/L</div>
  <div class="abs search">Search
    <svg width="9" height="9" viewBox="0 0 9 9"><circle cx="3.5" cy="3.5" r="2.6" fill="none" stroke="#333" stroke-width="1.3"/><line x1="5.4" y1="5.4" x2="8.5" y2="8.5" stroke="#333" stroke-width="1.6"/></svg>
  </div>
</header>

<section>
  <div class="abs hero" role="img" aria-label="Photo of a smiling family with children on their shoulders outdoors"></div>
  <div class="abs hero-panel"></div>
  <h2 class="abs hero-title">LOREM IPSUM DOLOR<br>SIT AMET</h2>
  <p class="abs hero-text">Lorem ipsum dolor sit amet, consectetuer adipiscing elit. Nam nibh. Nunc varius facilisis eros. Sed erat.In in velit quis arcuornare laoreet. Curabitur adipiscing luctus massa.</p>
  <div class="abs dots-tab"><span class="dot on"></span><span class="dot"></span><span class="dot"></span><span class="dot"></span><span class="dot"></span><span class="dot"></span></div>
</section>

<nav class="abs nav">
  <ul>
    <li>HOME</li><li>OVERVIEW</li><li>CURRENT PROJECTS</li><li>COMPLETED PROJECTS&nbsp;&nbsp;&nbsp;&nbsp;</li><li>FUTURE PROJECTS</li><li>LATEST NEWS</li><li>CONTACT US</li>
  </ul>
</nav>
<div class="abs dropdown">
  <div class="drop-item" style="top:6px">KT DEVLOPMENTS</div>
  <div class="drop-item" style="top:38px">TB BUILDERS</div>
</div>

<section>
  <article class="abs card dark" style="left:195px">
    <h3>CURRENT PROJECTS</h3>
    <div class="photo" role="img" aria-label="Photo of a two-storey house with a red front door" style="background:linear-gradient(#d8d4c8,#b7ad98 60%,#6f8a4a)"></div>
    <h4>LINWOOD TERRACES</h4>
    <p>Lorem Ipsum is simply dummy text Lorem Ipsum is simply &nbsp;dummy text</p>
    <div class="more">&gt;&gt;&nbsp; Details</div>
  </article>
  <article class="abs card" style="left:451px">
    <h3>COMPLETED PROJECTS</h3>
    <div class="photo" role="img" aria-label="Photo of a dark green completed family home" style="background:linear-gradient(#a9c7e6,#4b5a55 45%,#3d4a3c 75%,#6c8a3d)"></div>
    <h4>BANKSIA RISE</h4>
    <p>Lorem Ipsum is simply dummy text Lorem Ipsum is simply &nbsp;dummy text</p>
    <div class="more">&gt;&gt;&nbsp; Details</div>
  </article>
  <article class="abs card" style="left:708px">
    <h3>FUTURE PROJECTS</h3>
    <div class="photo" role="img" aria-label="Photo of a modern lit house at dusk" style="background:linear-gradient(#1f2a33,#3d5a63 45%,#7a4a2c 80%,#4d6a34)"></div>
    <h4>CRESTVIEW HILL</h4>
    <p>Lorem Ipsum is simply dummy text Lorem Ipsum is simply &nbsp;dummy text</p>
    <div class="more">&gt;&gt;&nbsp; Details</div>
  </article>
</section>

<section>
  <div class="abs welcome"></div>
  <h2 class="abs welcome-title">Welcome to&nbsp; <b>KT Developments P/L</b></h2>
  <div class="abs welcome-photo" role="img" aria-label="Photo of a single-storey home with palm trees and lawn"></div>
  <div class="abs welcome-text">
    <p>Lorem ipsum dolor sit amet, consectetuer adipiscing elit. Nam nibh. Nunc varius facilisis eros. Sed erat.&nbsp; Lorem ipsum dolor sit amet, consectetuer adipiscing elit. Nam nibh. Nunc varius facilisis eros. Sed erat. In in velit quis arcu ornare laoreet. Curabitur adipiscing luctus massa. Integer ut purus ac augue commodo commodo. Nunc nec mi eu justo tempor consectetuer. Etiam vitae nisl.</p>
  </div>
  <p class="abs link-more" style="left:445px;top:1002px"><span>&gt;&gt;</span>More</p>
  <div class="abs divider"></div>
  <h3 class="abs cat-title">OUR CATAGORIES</h3>
  <ul class="abs cats">
    <li>Lorem ipsum dolor sit amet</li><li>Lorem ipsum dolor sit amet</li><li>Lorem ipsum dolor sit amet</li>
    <li>Lorem ipsum dolor sit amet</li><li>Lorem ipsum dolor sit amet</li><li>Lorem ipsum dolor sit amet</li>
  </ul>
  <p class="abs link-more" style="left:865px;top:1023px"><span>&gt;&gt;</span>More</p>
</section>

<footer>
  <div class="abs footer"></div>
  <div class="abs fsep" style="left:371px"></div>
  <div class="abs fsep" style="left:684px"></div>

  <h3 class="abs ftitle" style="left:208px;top:1066px">Contact <em>Us</em></h3>
  <div class="abs faddr-h">Address</div>
  <p class="abs faddr">It has survived not centuries,</p>
  <svg class="abs" style="left:192px;top:1151px" width="17" height="17" viewBox="0 0 17 17"><rect width="17" height="17" rx="3" fill="#fff"/><path d="M5 3.5c-1 .6-1.5 1.6-1 3 .9 2.8 3 5 5.8 6.3 1.3.5 2.4 0 3-1l-2-1.8-1.3.8c-1.4-.7-2.4-1.8-3-3.1l.8-1.3z" fill="#151515"/></svg>
  <div class="abs phone" style="top:1151px">38415520 <span style="color:var(--orange-deep);font-weight:400;font-size:10px;margin-left:10px">or</span></div>
  <div class="abs phone" style="top:1174px">041296407</div>

  <h3 class="abs ftitle" style="left:417px;top:1066px">Connect <em>Us</em></h3>
  <div class="abs social">
    <i style="background:#2a64c0"></i><i style="background:#4cb9e8"></i><i style="background:#2f86c6"></i><i style="background:#f07a1a"></i>
  </div>
  <p class="abs flinks">Privacy Policy &nbsp;| &nbsp;Terms &amp; Conditions &nbsp;| &nbsp;Contact us</p>
  <p class="abs copy">© 2011 KT Developments, All Rights Reserved</p>

  <h3 class="abs ftitle" style="left:714px;top:1066px">Connect with <em>KT Developments</em></h3>
  <div class="abs flabel" style="left:714px;top:1105px">User Name &nbsp;:</div>
  <div class="abs finput" style="top:1100px"></div>
  <div class="abs flabel" style="left:714px;top:1138px">Email Address &nbsp;:</div>
  <div class="abs finput" style="top:1135px"></div>
  <div class="abs subscribe">Subscribe</div>
</footer>

</body>
</html>
```